Car rental website design for a UAE car rental company

This project is about creating a new website design for a car rental company located in Dubai (United Arab Emirates), I opened the same project a few months ago but I didn't receive a lot of appealing entries so I closed it but this time I am marking the project as guaranteed to avoid such situation again, if you have already provided a design before then please re-submit again on this project so that it is considered while reviewing all the designs

A few important things:

1- We need a simple non-complex design
2- The final deliverable would be 2 screens (PSD, JPEG ... etc), the first screen is for the home page and the second screen is for an internal page
3- The home page must have a section that end users can use to rent a car online directly from the home page instead of going into some inner pages
4- The current website is very old and not very appealing so avoid creating a similar design (www.quarvin-drive.example)
5- The name is Quarvin but the company rents normal cars (no Limousin cars will be rented) so avoid adding any fancy cars in the images/graphics used in the design, just normal end users cars
6- The expected pages would be: home, About us, Our team, Strategy, Contact us and links to social media pages
7- The attachments include the company's logo and some screens from other car rental companies that provide online rentals/payments

If you have any questions please feel free to ask and please note that we will need the designs urgently

Thanks

Target Market(s)

Dubai - United Arab Emirates

Industry/Entity Type

It Company

Number of Pages Required

2 page

Font styles to use
Sans Serif

Requirements
Must have
• Check the project details
Nice to have
Should not have

```html
<!DOCTYPE html>
<html lang="en">
<head>
<meta charset="utf-8">
<title>Quarvin – Car Rental</title>
<link rel="stylesheet" href="https://fonts.googleapis.com/css2?family=Oswald:wght@400;500&family=Open+Sans:wght@400;600;700&display=swap">
<style>
:root{
  --crimson:#a6103c;
  --crimson-dark:#8c0c31;
  --grey:#8b908d;
  --ink:#2a2a2a;
  --paper:#ffffff;
  --panel:#f4f4f4;
  --stage:#e8e6e2;
  --footer:#262626;
}
*{box-sizing:border-box;margin:0;padding:0}
html,body{width:1200px;height:1200px;overflow:hidden}
body{background:var(--stage);font-family:"Open Sans",Arial,sans-serif;color:var(--ink);font-size:10px}
.page{position:absolute;left:236px;top:15px;width:728px;height:1170px;background:var(--paper);box-shadow:0 2px 10px rgba(0,0,0,.18);overflow:hidden}

/* header */
.header{position:absolute;left:0;top:0;width:100%;height:105px}
.phone-tab{position:absolute;right:34px;top:0;width:162px;height:22px;background:var(--footer);color:#fff;border-radius:0 0 6px 6px;display:flex;align-items:center;justify-content:center;gap:6px;font-size:9px;letter-spacing:.5px}
.brand{position:absolute;left:56px;top:32px;display:flex;align-items:center;gap:8px}
.brand-mark{width:26px;height:26px;background:var(--crimson)}
.brand-name{font-family:"Oswald",sans-serif;font-size:26px;font-weight:400;color:var(--grey);line-height:1}
.contact-line{position:absolute;right:34px;top:60px;display:flex;align-items:center;gap:10px}
.email{font-size:11px;color:var(--crimson)}
.email span{color:var(--grey);font-size:9.5px}
.social{display:flex;gap:8px}
.social i{display:block;width:25px;height:25px;background:var(--crimson);transform:rotate(45deg) scale(.8);border-radius:4px}

/* nav */
.nav{position:absolute;left:0;top:105px;width:100%;height:31px;background:var(--crimson);display:flex;justify-content:space-around;align-items:center;padding:0 20px;border-bottom:3px solid var(--crimson-dark)}
.nav a{color:#fff;text-decoration:none;font-size:10px;font-weight:600;letter-spacing:.3px}

/* hero */
.hero{position:absolute;left:0;top:136px;width:100%;height:315px;border-bottom:1px solid #e2e2e2}
.hero-copy{position:absolute;left:46px;top:20px;width:370px}
.hero-title{font-family:"Oswald",sans-serif;font-size:42px;font-weight:500;color:var(--crimson);line-height:1.1}
.hero-title span{color:var(--grey)}
.hero-lead{margin-top:6px;color:var(--crimson);font-size:10.5px;line-height:1.45}
.hero-text{margin-top:8px;font-size:9px;line-height:1.6}
.btn{display:inline-flex;align-items:center;justify-content:space-between;gap:8px;background:var(--crimson);color:#fff;font-size:7px;font-weight:700;text-transform:uppercase;padding:4px 8px;border-radius:2px}
.btn::after{content:"";border-left:5px solid #fff;border-top:4px solid transparent;border-bottom:4px solid transparent}
.hero .btn{margin-top:12px;width:72px}
.hero-car{position:absolute;left:123px;top:184px;width:236px;height:118px;border-radius:40% 45% 18% 18%/55% 55% 25% 25%;background:linear-gradient(180deg,#c9cdd0,#8f959a 70%,#5a5f63)}

/* booking */
.booking{position:absolute;left:424px;top:10px;width:272px;height:290px;background:var(--panel);border-bottom:2px solid var(--crimson)}
.tabs{display:flex;height:24px}
.tab{flex:1;display:flex;align-items:center;justify-content:center;font-family:"Oswald",sans-serif;font-size:9px;color:#fff;background:var(--grey);border-radius:5px 5px 0 0}
.tab.active{background:var(--crimson);flex:.75}
.booking-body{padding:10px 12px;font-size:8px}
.row{display:flex;align-items:center;gap:5px;margin-bottom:8px}
.label{width:92px;color:var(--crimson)}
.field{background:#fff;border:1px solid #ddd;height:16px;padding:0 4px;display:flex;align-items:center;font-size:7.5px}
.field.date{width:62px}
.field.num{width:26px}
.field.wide{width:126px;justify-content:space-between}
.field.wide b{width:10px;height:14px;background:#333}
.cal{width:10px;height:10px;background:var(--crimson)}
.days{text-align:right;color:var(--crimson);font-size:10px;margin:2px 0 10px}
.section-label{font-size:10.5px;margin-bottom:10px;padding-top:4px;border-top:1px solid #ddd}
.opt{display:flex;align-items:center;gap:5px;color:var(--crimson);margin-bottom:8px}
.opt i{width:8px;height:8px;border:1px solid #999;background:#fff;display:block}
.opt i.round{border-radius:50%}
.opts{display:flex;gap:80px}
.quote{margin-left:auto;background:var(--crimson);color:#fff;font-size:8px;font-weight:700;padding:3px 10px;border-radius:2px}

/* gallery */
.gallery{position:absolute;left:0;top:451px;width:100%;height:224px;background:linear-gradient(180deg,#f1f1f1,#fff)}
.heading{font-family:"Oswald",sans-serif;font-size:18px;color:var(--crimson);font-weight:400;line-height:1.2}
.gallery .heading{position:absolute;left:62px;top:12px}
.gallery-car{position:absolute;left:59px;top:60px;width:284px;height:104px;border-radius:45% 50% 18% 18%/60% 60% 25% 25%;background:linear-gradient(180deg,#d2d5d7,#959b9f 70%,#60656a)}
.gallery-copy{position:absolute;left:400px;top:84px;width:320px;text-align:center}
.gallery-copy h3{font-family:"Oswald",sans-serif;font-size:21px;font-weight:500;letter-spacing:.5px;line-height:1.2}
.gallery-copy h3 span{color:var(--crimson);text-decoration:underline}
.gallery-copy p{font-family:"Oswald",sans-serif;color:var(--grey);font-size:16px;margin-top:4px}
.gallery-copy .btn{margin-top:10px;width:90px}
.arrows{position:absolute;left:388px;top:194px;display:flex;gap:8px}
.arrows span{width:18px;height:18px;border:1px solid var(--crimson);display:flex;align-items:center;justify-content:center}

/* mission */
.mission{position:absolute;left:34px;top:675px;width:662px;height:203px;background:var(--crimson);color:#fff}
.mission-tab{position:absolute;left:30px;top:8px;background:#fff;padding:2px 18px;font-family:"Oswald",sans-serif;font-size:17px;color:var(--ink);border-bottom:2px solid #ccc}
.mission-rule{position:absolute;left:30px;right:230px;top:38px;height:1px;background:rgba(255,255,255,.5)}
.mission-text{position:absolute;left:46px;top:48px;width:345px;font-size:9px;line-height:13.3px}
.mission-text p+p{margin-top:4px}
.mission .btn{position:absolute;left:46px;top:168px;background:#fff;color:var(--crimson);width:80px}
.mission .btn::after{border-left-color:var(--crimson)}
.mission-photo{position:absolute;right:55px;top:20px;width:142px;height:162px;background:linear-gradient(180deg,#e9e6e0,#b9b3aa 60%,#3a3d44)}

/* service */
.service{position:absolute;left:0;top:886px;width:100%;padding:0 80px 0 104px}
.service .heading{margin-left:-4px}
.service-intro{font-size:11.5px;font-weight:600;margin:6px 0 10px 20px;line-height:1.35}
.service-cols{display:flex;gap:50px;margin-left:20px;font-size:8.5px;line-height:12px}
.service-cols ul{list-style:none}
.service-cols > ul{width:260px}
.service-cols > ul > li{display:flex;gap:6px;align-items:flex-start;margin-bottom:4.8px}
.tick{flex:none;width:10px;height:10px;margin-top:1px}
.sub{list-style:none;margin:1px 0 0 18px}
.sub li{line-height:12.4px}
.sub li::before{content:"– ";}

/* footer */
.footer{position:absolute;left:0;top:1099px;width:100%;height:35px;background:var(--footer);display:flex;align-items:center;padding:0 40px 0 60px;gap:38px}
.footer a{color:#fff;text-decoration:none;font-size:9.5px}
.footer .social{margin-left:auto}
.copyright{position:absolute;left:0;top:1148px;width:100%;text-align:center;font-size:9.5px}
</style>
</head>
<body>
<div class="page">
  <header class="header">
    <div class="phone-tab">
      <svg width="10" height="10" viewBox="0 0 24 24"><path fill="#fff" d="M6.6 10.8a15 15 0 006.6 6.6l2.2-2.2c.3-.3.7-.4 1-.2 1.1.4 2.3.6 3.6.6.6 0 1 .4 1 1V20c0 .6-.4 1-1 1A17 17 0 013 4c0-.6.4-1 1-1h3.5c.6 0 1 .4 1 1 0 1.3.2 2.5.6 3.6.1.3 0 .7-.2 1z"/></svg>
      +971 4000 1234
    </div>
    <div class="brand"><span class="brand-mark"></span><span class="brand-name">Quarvin</span></div>
    <div class="contact-line">
      <div class="email">Email Us : <span>hello@quarvin-drive.example</span></div>
      <div class="social"><i></i><i></i><i></i><i></i></div>
    </div>
  </header>

  <nav class="nav">
    <a href="#">HOME</a><a href="#">ABOUT US</a><a href="#">OUR TEAM</a><a href="#">STRATEGY</a><a href="#">CONTACT US</a><a href="#">GALLERY</a>
  </nav>

  <section class="hero">
    <div class="hero-copy">
      <h1 class="hero-title">Welcome To <span>Quarvin</span></h1>
      <p class="hero-lead">As Dubai is expected to welcome millions of tourists and visitors, car rental industry is believed to escalate more rapidly in the region.</p>
      <p class="hero-text">Over the past five years, demands for car rentals in Dubai has been augmenting at a healthy pace and is currently registering a growth rate of 20 to 25 percent per year. The swift economic growth and the number...</p>
      <span class="btn">Read more</span>
    </div>
    <div class="hero-car" role="img" aria-label="Silver family sedan"></div>

    <div class="booking">
      <div class="tabs"><div class="tab active">Book a Car</div><div class="tab">View,modify or cancel a booking</div></div>
      <div class="booking-body">
        <div class="row"><span class="label">Rental Start Date/Time</span><span class="field date">27 March 2015</span><span class="cal"></span><span class="field num">10</span><span class="field num">00</span></div>
        <div class="row"><span class="label">Rental End Date/Time</span><span class="field date">29 March 2015</span><span class="cal"></span><span class="field num">10</span><span class="field num">00</span></div>
        <div class="days">Number of Days 2</div>
        <div class="section-label">Pick-up Location(City, State or Airport Code)</div>
        <div class="opts"><div class="opt"><i class="round"></i>Choose Station</div><div class="opt"><i class="round"></i>Choose Car Type</div></div>
        <div class="opt"><i></i>Returning to Same as pickup location</div>
        <div class="row"><span class="label">Pickup rental country</span><span class="field wide">Dubai<b></b></span></div>
        <div class="row"><span class="label">Rental location</span><span class="field wide"></span></div>
        <div class="row"><span class="label">Sign Up your account</span><span class="field wide">Select an account type<b></b></span></div>
        <div class="row"><span class="opt" style="margin:0"><i></i>Apply any discount Code</span><span class="quote">Get Quote</span></div>
      </div>
    </div>
  </section>

  <section class="gallery">
    <h2 class="heading">Gallary</h2>
    <div class="gallery-car" role="img" aria-label="Silver hatchback car, side view"></div>
    <div class="gallery-copy">
      <h3>EXPERIENCE AN <span>EXTRA</span> MILE</h3>
      <p>of comfort, pleasure and leisure from the best</p>
      <span class="btn">Read more</span>
    </div>
    <div class="arrows">
      <span><svg width="8" height="8" viewBox="0 0 8 8"><path d="M6 0L1 4l5 4" fill="none" stroke="#a6103c" stroke-width="1.6"/></svg></span>
      <span><svg width="8" height="8" viewBox="0 0 8 8"><path d="M2 0l5 4-5 4" fill="none" stroke="#a6103c" stroke-width="1.6"/></svg></span>
    </div>
  </section>

  <section class="mission">
    <div class="mission-tab">Mission &amp; Vision</div>
    <div class="mission-rule"></div>
    <div class="mission-text">
      <p>No sit feugiat consetetur volutpat et. Iriure magna ut at eirmod vero odio blandit sea gubergren lorem. Labore ea eu lorem sed labore feugiat ullamcorper. Dolor no ut augue rebum sanctus esse illum sadipscing exerci. Sanctus placerat eirmod ut amet sit et et lorem.</p>
      <p>No sit feugiat consetetur volutpat et. Iriure magna ut at eirmod vero odio blandit sea gubergren lorem. Labore ea eu lorem sed labore feugiat ullamcorper. Dolor no ut augue rebum sanctus esse illum sadipscing exerci. Sanctus placerat eirmod ut amet sit et et lorem.</p>
    </div>
    <span class="btn">Read more</span>
    <div class="mission-photo" role="img" aria-label="Portrait photo of a team member in a suit"></div>
  </section>

  <section class="service">
    <h2 class="heading">Service</h2>
    <p class="service-intro">Quarvin offers a comprehensive range of services including daily, short term and long term rental, chauffeur drive services for every purpose and budget.</p>
    <div class="service-cols">
      <ul>
        <li><svg class="tick" viewBox="0 0 10 10"><circle cx="5" cy="5" r="4.3" fill="none" stroke="#333"/><path d="M3 5l1.5 1.5L7 3.5" fill="none" stroke="#333"/></svg>Wide range of vehicles for city driving or SUV's for trips</li>
        <li><svg class="tick" viewBox="0 0 10 10"><circle cx="5" cy="5" r="4.3" fill="none" stroke="#333"/><path d="M3 5l1.5 1.5L7 3.5" fill="none" stroke="#333"/></svg>Special 10% discount for new customers on the first rent</li>
        <li><svg class="tick" viewBox="0 0 10 10"><circle cx="5" cy="5" r="4.3" fill="none" stroke="#333"/><path d="M3 5l1.5 1.5L7 3.5" fill="none" stroke="#333"/></svg><div>Long term car rental
          <ul class="sub"><li>New vehicles</li><li>Fixed monthly expenditure</li><li>Free registration and insurance</li><li>Free maintenance and replacement vehicles</li><li>No finance costs and no hidden costs</li></ul></div></li>
      </ul>
      <ul>
        <li><svg class="tick" viewBox="0 0 10 10"><circle cx="5" cy="5" r="4.3" fill="none" stroke="#333"/><path d="M3 5l1.5 1.5L7 3.5" fill="none" stroke="#333"/></svg>sightseeing tours</li>
        <li><svg class="tick" viewBox="0 0 10 10"><circle cx="5" cy="5" r="4.3" fill="none" stroke="#333"/><path d="M3 5l1.5 1.5L7 3.5" fill="none" stroke="#333"/></svg>Buyback option after lease term</li>
        <li><svg class="tick" viewBox="0 0 10 10"><circle cx="5" cy="5" r="4.3" fill="none" stroke="#333"/><path d="M3 5l1.5 1.5L7 3.5" fill="none" stroke="#333"/></svg>Special offers for online bookings</li>
        <li><svg class="tick" viewBox="0 0 10 10"><circle cx="5" cy="5" r="4.3" fill="none" stroke="#333"/><path d="M3 5l1.5 1.5L7 3.5" fill="none" stroke="#333"/></svg>airport transfers</li>
      </ul>
    </div>
  </section>

  <footer class="footer">
    <a href="#">HOME</a><a href="#">ABOUT US</a><a href="#">OUR TEAM</a><a href="#">STRATEGY</a><a href="#">CONTACT US</a><a href="#">GALLERY</a>
    <div class="social"><i></i><i></i><i></i><i></i></div>
  </footer>
  <p class="copyright">@Copyright 2015, Quarvin. ALL RIGHTS RESERVED.</p>
</div>
</body>
</html>
```